we can communicate on this, but i want to follow the approach we took on Pell|Quorn & Tillet but i feel the card front needs the black background and the platinum and gold logo. The back? I am open. we can use the same info from PQ&T. Vellum Crest is an enhanced equity investment fund - basically a very exclusive boutique hedge fund that uses only stock options. very advanced things. hope you are interested

Contact Information for Business Card

Dr. Owen T. Brisket, CFA
Scientifique de fusée financière
555.014.2296
TheDoc4793@mailvessel.example

4718 Fennel Brook Way N.
West Fargo, ND 58078

No web site

Colors

Designer to choose colors to be used in the design.

Requirements
Nice to have
• I tend to prefer the most visible applications of the logo to include logo and name, the logo version with a black background and the gold and platinum components separated by the black. I see this working well for a single side (logo and name - this is card front to me).
• I am fairly open to other treatments on the reverse side with the data. To me, it makes sense to have a different color rendition of the logo on the reverse and it may be a muted black tone on tone or an oversized portion that would have spot UV. Or, the reverse may play with colors and layout
Should not have
• Other colors = no no
• Decorative font

```html
<!DOCTYPE html>
<html lang="en">
<head>
<meta charset="utf-8">
<title>Vellum Crest — Business Card</title>
<link rel="stylesheet" href="https://fonts.googleapis.com/css2?family=Roboto:wght@400;500;700&display=swap">
<style>
  :root {
    --backdrop: #2a2a2c;
    --card-black: #141416;
    --gold: #c9a73e;
    --gold-light: #d6b653;
    --platinum: #bdbdbd;
    --white: #ffffff;
  }
  * { box-sizing: border-box; margin: 0; padding: 0; }
  html, body {
    width: 1200px; height: 960px; overflow: hidden;
    background: var(--backdrop);
    font-family: "Roboto", Arial, sans-serif;
  }
  .canvas { position: relative; width: 1200px; height: 960px; }

  .card {
    position: absolute;
    width: 700px; height: 400px;
    border-radius: 4px;
    overflow: hidden;
    box-shadow: 0 18px 40px rgba(0,0,0,.45);
  }

  /* Front */
  .card--front { left: 80px; top: 60px; background: var(--card-black); }
  .front-brand {
    position: absolute; left: 0; right: 0; top: 110px;
    display: flex; flex-direction: column; align-items: center; gap: 22px;
  }
  .brand-disc {
    width: 120px; height: 120px; border-radius: 50%;
    background: var(--platinum);
  }
  .brand-name {
    font-weight: 700; font-size: 40px; letter-spacing: 3px;
    text-transform: uppercase; color: var(--platinum);
  }

  /* Back */
  .card--back { left: 420px; top: 500px; background: var(--gold); }
  .back-field { position: absolute; inset: 0; }
  .back-brand {
    position: absolute; right: 40px; top: 34px;
    display: flex; flex-direction: column; align-items: center; gap: 14px;
  }
  .back-brand .brand-disc { width: 84px; height: 84px; background: var(--gold-light); }
  .back-brand .brand-name { font-size: 30px; color: var(--white); letter-spacing: 2px; }

  .holder { position: absolute; left: 42px; top: 92px; color: var(--white); }
  .holder-name { font-weight: 700; font-size: 22px; }
  .holder-name small { font-weight: 400; font-size: 13px; }
  .holder-title { font-size: 14px; margin-top: 4px; }

  .contact {
    position: absolute; left: 42px; bottom: 40px;
    color: var(--white); font-size: 14px; line-height: 1.45;
  }
  .contact-address { margin-bottom: 12px; }
  .contact-list { list-style: none; }
  .contact-list li { display: flex; align-items: center; gap: 10px; }
  .contact-list svg { width: 13px; height: 13px; fill: var(--white); flex: none; }
</style>
</head>
<body>
<main class="canvas">

  <section class="card card--front" aria-label="Card front">
    <div class="front-brand">
      <span class="brand-disc"></span>
      <span class="brand-name">Vellum Crest</span>
    </div>
  </section>

  <section class="card card--back" aria-label="Card back">
    <svg class="back-field" viewBox="0 0 700 400" preserveAspectRatio="none" aria-hidden="true">
      <path d="M290 0 C262 70 262 150 300 190 C335 225 390 165 455 160 C520 155 500 300 520 400 L700 400 L700 0 Z"
            fill="var(--card-black)"/>
    </svg>

    <div class="back-brand">
      <span class="brand-disc"></span>
      <span class="brand-name">Vellum Crest</span>
    </div>

    <div class="holder">
      <p class="holder-name">Dr. Owen T. Brisket, <small>CFA</small></p>
      <p class="holder-title">Scientifique de fusée financière</p>
    </div>

    <div class="contact">
      <p class="contact-address">4718 Fennel Brook Way N.<br>West Fargo, ND 58078</p>
      <ul class="contact-list">
        <li><svg viewBox="0 0 16 16"><path d="M4 0h8a1 1 0 0 1 1 1v14a1 1 0 0 1-1 1H4a1 1 0 0 1-1-1V1a1 1 0 0 1 1-1zm1 2v10h6V2zm3 11a1 1 0 1 0 0 2 1 1 0 0 0 0-2z"/></svg>555.014.2296</li>
        <li><svg viewBox="0 0 16 16"><path d="M0 3h16v10H0zm1.5 1.2V12h13V4.2L8 9z"/></svg>TheDoc4793@mailvessel.example</li>
      </ul>
    </div>
  </section>

</main>
</body>
</html>
```